Real estate business card

I need a business card for my real estate company. I help clients buy and sell properties. I would like to keep the design very simple and professional. I would like the design to convey professionalism, safety and trust. I prefer no graphics but a simple logo design would be nice if that is part of what you do.
Updates

Please keep the designs simple. No high-rise buildings please. 

Target Market(s)

Age group 30-60 mostly affluent

Industry/Entity Type

Real Estate

Contact Information for Business Card

Venkell Realtors
Bernard Venkell, Broker
5146 Marrow Ave. #327, La Crescenta, CA 91214

Requirements
Nice to have
• Logo can be combination of my initials BV or just Z or a simple geometric shape? Please see "Desig Ideas" attachment. No pics of houses or shaking hands, dollar bills, $, %, etc...
Please use fonts similar to Helvetica for a clean, modern look (think Northern European design, simple, clean yet bold)

Also use font colors such as blue, grey in different shades. Use pastel colors if better.

```html
<!DOCTYPE html>
<html lang="en">
<head>
<meta charset="utf-8">
<title>Venkell Realtors – Business Card</title>
<link rel="stylesheet" href="https://fonts.googleapis.com/css2?family=Roboto:wght@300;400;500;700&display=swap">
<style>
  :root {
    --brand-blue: #1b84b6;
    --brand-blue-deep: #166f9c;
    --paper: #f7f7f7;
    --paper-shade: #e9e9e9;
    --rule-grey: #a9a9a9;
    --logo-grey: #8c8c8c;
    --text-light: #ffffff;
    --text-soft: #d6ebf5;
    --backdrop: #e4e6e8;
  }
  * { margin: 0; padding: 0; box-sizing: border-box; }
  html, body {
    width: 1200px;
    height: 852px;
    overflow: hidden;
    background: var(--backdrop);
    font-family: "Roboto", "Helvetica Neue", Arial, sans-serif;
  }
  .canvas {
    position: relative;
    width: 1200px;
    height: 852px;
  }
  .business-card {
    position: absolute;
    left: 75px;
    top: 126px;
    width: 1050px;
    height: 600px;
    background: var(--brand-blue);
    overflow: hidden;
    box-shadow: 0 6px 24px rgba(0, 0, 0, 0.15);
  }
  .top-band {
    position: absolute;
    left: 0; top: 0;
    width: 100%;
    height: 92px;
    background: linear-gradient(180deg, var(--brand-blue-deep), var(--brand-blue));
  }
  .top-band .inner-rule {
    position: absolute;
    left: 0; right: 0;
    bottom: 14px;
    height: 3px;
    background: var(--paper);
  }
  .name-band {
    position: absolute;
    left: 0; top: 92px;
    width: 100%;
    height: 220px;
    background: linear-gradient(180deg, var(--paper), var(--paper-shade));
    border-top: 3px solid var(--rule-grey);
    border-bottom: 3px solid var(--rule-grey);
    display: flex;
    align-items: center;
    justify-content: center;
  }
  .wordmark {
    display: flex;
    align-items: center;
    gap: 22px;
  }
  .wordmark-mark {
    width: 46px;
    height: 46px;
    background: var(--logo-grey);
  }
  .wordmark-name {
    font-weight: 700;
    font-size: 64px;
    letter-spacing: 1px;
    color: var(--brand-blue);
  }
  .contact-band {
    position: absolute;
    left: 0; top: 312px;
    width: 100%;
    height: 288px;
    background: linear-gradient(180deg, var(--brand-blue), var(--brand-blue-deep));
    color: var(--text-light);
  }
  .person {
    position: absolute;
    left: 84px;
    bottom: 70px;
  }
  .person-name {
    font-size: 34px;
    letter-spacing: 0.5px;
    text-transform: uppercase;
  }
  .person-name .given { font-weight: 700; }
  .person-name .family { font-weight: 300; }
  .person-role {
    margin-top: 4px;
    font-size: 19px;
    font-weight: 300;
    letter-spacing: 1px;
    text-transform: uppercase;
    color: var(--text-soft);
  }
  .contact-list {
    position: absolute;
    left: 560px;
    top: 36px;
    padding-left: 26px;
    border-left: 1px solid rgba(255, 255, 255, 0.45);
    list-style: none;
  }
  .contact-item {
    display: flex;
    align-items: center;
    gap: 14px;
    font-size: 19px;
    font-weight: 400;
    line-height: 1;
    padding: 8px 0;
  }
  .contact-item.phone { font-weight: 700; }
  .contact-icon {
    width: 18px;
    height: 18px;
    flex: none;
    fill: var(--text-light);
  }
</style>
</head>
<body>
<main class="canvas">
  <article class="business-card">
    <div class="top-band"><span class="inner-rule"></span></div>

    <section class="name-band">
      <div class="wordmark">
        <span class="wordmark-mark"></span>
        <span class="wordmark-name">Venkell Realtors</span>
      </div>
    </section>

    <section class="contact-band">
      <div class="person">
        <p class="person-name"><span class="given">Bernard</span> <span class="family">Venkell</span></p>
        <p class="person-role">Broker</p>
      </div>

      <ul class="contact-list">
        <li class="contact-item phone">
          <svg class="contact-icon" viewBox="0 0 24 24" aria-hidden="true"><path d="M6.6 10.8a15.2 15.2 0 0 0 6.6 6.6l2.2-2.2c.3-.3.7-.4 1-.2 1.1.4 2.3.6 3.6.6.6 0 1 .4 1 1V20c0 .6-.4 1-1 1A17 17 0 0 1 3 4c0-.6.4-1 1-1h3.5c.6 0 1 .4 1 1 0 1.3.2 2.5.6 3.6.1.3 0 .7-.2 1z"/></svg>
          <span>000 000 000</span>
        </li>
        <li class="contact-item email">
          <svg class="contact-icon" viewBox="0 0 24 24" aria-hidden="true"><path d="M3 5h18v14H3z M4.5 6.5 12 12l7.5-5.5" fill="none" stroke="#fff" stroke-width="2"/></svg>
          <span>hello@venkellrealtors.com</span>
        </li>
        <li class="contact-item address">
          <svg class="contact-icon" viewBox="0 0 24 24" aria-hidden="true"><path d="M12 2a7 7 0 0 0-7 7c0 5.2 7 13 7 13s7-7.8 7-13a7 7 0 0 0-7-7zm0 9.5A2.5 2.5 0 1 1 12 6.5a2.5 2.5 0 0 1 0 5z"/></svg>
          <span>5146 Marrow Ave. #327, La Crescenta, CA 91214</span>
        </li>
      </ul>
    </section>
  </article>
</main>
</body>
</html>
```